依頼詳細
“健康な街づくり”をテーマに地域への情報発信として、
他のクリニックとの対談ページを作成して参りました。
過去には下記内容の対談を行なっています。
①“内科✖️眼科による糖尿病治療から健康な街作り”
②“消化器内科✖️呼吸器内科によるがん検診から生活習慣病まで”へという内容です。
※過去のバナーについては下記の当院ホームページからご参照下さい。
https://morino-clinic-site.jp

今回は第3弾として、
“内科クリニック(内科医)✖️調剤薬局(薬剤師2名)による対談”
地域医療におけるかかりつけ医・かかりつけ薬局のあり方や、
それぞれの重要性について説明しています。

バナーはホームページやwebでの情報発信、Facebook投稿などで使用します。

完成後に別途院内・薬局内で掲示するポスター作成を予定しております。
記載項目
クリニックロゴ+森野クリニック対談(左上端に小さめで)
それぞれの写真、名前
森野クリニック 森野健吾(主催者)
緑陽舎薬局 大塚花音
岡沢薬局 桑原進

“地域におけるチーム医療”+下記のいずれかの文言
“健康な街づくりへ”
“人生笑って100まで生きる クリニックからの提案”
サイズ
• 250 x 250 ( スクエアポップアップ )
• 970✖️250、320✖️100、420✖️594
希望イメージ
シンプル 複雑
単色 カラフル
暗い 明るい
日常 高級
遊び心 厳粛
未来的 伝統的
女性的 男性的
希望する色
納品ファイル
• 高解像度JPG (.jpg)
• PNG形式 (.png)
補足説明
クリニックロゴ添付致します。
写真は下記よりダウンロード願います。
https://qwd-share.jp/Kt7rPa
Pass: mkforumx
■ 選んだ理由

かかりつけ薬局のイメージに合った暖かいデザイン。

■ 提案者全員のお礼・コメント

当院バナーのデザインを作成頂きありがとうございました。
素敵なデザインが多く迷いましたが、
かかりつけ薬局のイメージに近いものを採用させて頂きました。

```html
<!DOCTYPE html>
<html lang="ja">
<head>
<meta charset="utf-8">
<title>森野クリニック対談 地域におけるチーム医療</title>
<link rel="stylesheet" href="https://fonts.googleapis.com/css2?family=Shippori+Mincho:wght@500;700;800&display=swap">
<style>
  :root {
    --bg-top: #eef5fb;
    --bg-mid: #d6e7f4;
    --bg-bottom: #a9cbe6;
    --brand-blue: #2f72a8;
    --pill-dark: #1f5f93;
    --pill-light: #3a83bd;
    --logo-teal: #5aaeb8;
    --ink: #2c3a4a;
    --frame: #ffffff;
    --label-pink: #e3b3c4;
    --label-yellow: #ecd17a;
    --label-green: #a9e58f;
  }
  * { margin: 0; padding: 0; box-sizing: border-box; }
  html, body { width: 1200px; height: 1200px; overflow: hidden; }
  body {
    font-family: "Shippori Mincho", serif;
    color: var(--ink);
  }
  .banner {
    position: relative;
    width: 1200px;
    height: 1200px;
    overflow: hidden;
    background:
      radial-gradient(ellipse at 30% 25%, #ffffff 0%, rgba(255,255,255,0) 55%),
      linear-gradient(170deg, var(--bg-top) 0%, var(--bg-mid) 50%, var(--bg-bottom) 100%);
  }
  .clinic-logo {
    position: absolute;
    left: 30px; top: 30px;
    width: 276px; height: 78px;
    background: #fff;
    display: flex; align-items: center; gap: 12px;
    padding-left: 16px;
  }
  .clinic-logo .mark {
    flex: none;
    width: 38px; height: 38px; border-radius: 50%;
    background: var(--logo-teal);
  }
  .clinic-logo .name {
    font-size: 26px; font-weight: 500; color: var(--logo-teal);
    letter-spacing: 1px;
    white-space: nowrap;
  }
  .series-title {
    position: absolute;
    left: 36px; top: 132px;
    font-size: 24px; font-weight: 700; color: var(--ink);
    letter-spacing: 1px;
    white-space: nowrap;
  }
  .theme-pill {
    position: absolute;
    left: 528px; top: 82px;
    width: 606px; height: 100px;
    border-radius: 50px;
    background: linear-gradient(90deg, var(--pill-dark), var(--pill-light));
    box-shadow: 0 6px 10px rgba(30,70,110,0.3);
    display: flex; align-items: center; justify-content: center;
    color: #fff; font-size: 46px; font-weight: 700; letter-spacing: 3px;
    white-space: nowrap;
  }
  .headline {
    position: absolute;
    left: 40px; top: 218px;
    width: 1130px;
    text-align: center;
    font-size: 84px; font-weight: 800;
    color: var(--brand-blue);
    letter-spacing: 2px;
    white-space: nowrap;
    text-shadow: 0 2px 2px rgba(255,255,255,0.8);
  }
  .portrait-card {
    position: absolute;
    background: var(--frame);
    box-shadow: 0 6px 16px rgba(40,80,120,0.25);
    padding: 20px;
  }
  .portrait-card .photo { width: 100%; }
  .portrait-card .name-tag {
    margin: 22px auto 0;
    border-radius: 30px;
    display: flex; flex-direction: column; align-items: center; justify-content: center;
    font-size: 26px; font-weight: 700; color: var(--ink);
    letter-spacing: 2px; line-height: 1.35; text-align: center;
    white-space: nowrap;
  }
  .card-center { left: 358px; top: 414px; width: 410px; height: 474px; transform: rotate(-1.5deg); z-index: 1; }
  .card-center .photo { height: 352px; background: linear-gradient(135deg, #e9edf1 0%, #cfe3ec 45%, #3fa6c3 75%, #dfe8ee 100%); }
  .card-center .name-tag { width: 304px; height: 64px; background: var(--label-pink); margin: 18px 0 0 auto; font-size: 24px; }
  .card-left { left: 4px; top: 666px; width: 420px; height: 504px; transform: rotate(-2.5deg); z-index: 2; }
  .card-left .photo { height: 368px; background: linear-gradient(135deg, #f1ece6 0%, #e2ddd7 40%, #3a3f4a 70%, #c6d6e6 100%); }
  .card-left .name-tag { width: 340px; height: 70px; background: var(--label-yellow); }
  .card-right { left: 768px; top: 678px; width: 420px; height: 492px; transform: rotate(2.5deg); z-index: 2; }
  .card-right .photo { height: 360px; background: linear-gradient(135deg, #eef1f3 0%, #dfe5ea 40%, #23473c 70%, #c9d8e4 100%); }
  .card-right .name-tag { width: 336px; height: 72px; background: var(--label-green); font-size: 23px; }
</style>
</head>
<body>
<main class="banner">
  <div class="clinic-logo">
    <span class="mark"></span>
    <span class="name">森野クリニック</span>
  </div>
  <p class="series-title">森野クリニック対談</p>

  <div class="theme-pill">健康な街づくりへ</div>
  <h1 class="headline">“地域におけるチーム医療”</h1>

  <figure class="portrait-card card-center">
    <div class="photo" role="img" aria-label="白衣姿の薬剤師 大塚花音の写真"></div>
    <figcaption class="name-tag">緑陽舎薬局　大塚花音</figcaption>
  </figure>

  <figure class="portrait-card card-left">
    <div class="photo" role="img" aria-label="スーツ姿の薬剤師 桑原進の写真"></div>
    <figcaption class="name-tag">岡沢薬局　桑原進</figcaption>
  </figure>

  <figure class="portrait-card card-right">
    <div class="photo" role="img" aria-label="スクラブ姿の医師 森野健吾の写真"></div>
    <figcaption class="name-tag"><span>森野クリニック</span><span>森野健吾（主催者）</span></figcaption>
  </figure>
</main>
</body>
</html>
```